Coral Meridian 6x6m trade show booth, Wall Design

Project Overview:
Our technology company is preparing for an upcoming trade show where we will showcase various products and divisions, including thermal radars, sonar, rapid deployment solutions for perimeter security, a tactical trailer, drone technology, and our new and emerging technology division. We are seeking a graphic design for our trade show walls that will tie together all these elements while staying true to our brand identity.
Objectives:
Create a cohesive and visually appealing graphic design that integrates all elements of our trade show booth.
Emphasize our company's identity by featuring our logo and utilizing our brand colours.
Maintain a minimalistic design to ensure that our stand does not appear cluttered given the numerous elements on display.
Key Information:
Design Elements:
1. Logo Integration:
Place the company logo prominently on the trade show wall to establish brand presence.
2. Color Palette:
Use our brand colours throughout the design to maintain consistency and brand recognition.
3. Minimalistic Design:
Ensure that the design is clean and minimal to avoid overwhelming visitors with too much visual information.
4. Visual Hierarchy:
Organize the elements on the wall in a way that guides the viewer's eye naturally from one section to another.

The design should convey a sense of innovation, cutting-edge technology, and professionalism. It should inspire confidence in our products and services while being approachable.
Please feel free to ask for any additional information or clarification as needed. We are looking forward to a design that effectively represents our brand and products at the trade show. Thank you for your creative input and expertise in advance.
I have attached a detailed brief in the downloads with addition text and information to give further context to our company and also the event we will be attending.
Updates

After discussions with our team, they have decided to take a different approach and have on design replicated on both walls. this design will be one image across all panels with key words across the tob as well as our logo. please see updated design breif for details.

Target Market(s)

Professionals in Defence, Government and Critical Infrastructure

Industry/Entity Type

Defence, Government and Critical Infrastructure

Font styles to use
Sans Serif

Colors
0054AA
0677BA
7BADD7
CADEEF
E8F1F8

Requirements
Must have
• My project must have clear brand awareness and utilise the wall space provided with a cohesive design. The design must be in line with the artwork requirements provided in the downloadable brief.
Nice to have
• It would be nice to have a minimalist design while still standing out
Should not have
• No clutter, any information to be diplayed in a clean and consice manner.

```html
<!DOCTYPE html>
<html lang="en">
<head>
<meta charset="utf-8">
<title>Coral Meridian – Booth Wall Artwork</title>
<link rel="stylesheet" href="https://fonts.googleapis.com/css2?family=Lato:wght@400;700&display=swap">
<style>
  :root {
    --page-bg: #f2f4f6;
    --header-bg: #ffffff;
    --navy: #0d2a5c;
    --brand-cyan: #1a9fcb;
    --divider: #c9d3de;
    --target-red: #e0231c;
    --sky-top: #3d7fd6;
    --sky-mid: #7fb3ea;
    --horizon: #a9cdf0;
    --sea-top: #2e5f9c;
    --sea-mid: #1f5e97;
    --sea-deep: #1c78b2;
    --sea-floor: #154e80;
  }
  * { box-sizing: border-box; margin: 0; padding: 0; }
  html, body {
    width: 1200px; height: 941px; overflow: hidden;
    background: var(--page-bg);
    font-family: "Lato", sans-serif;
  }
  .wall {
    position: absolute;
    left: 20px; top: 350px;
    width: 1160px; height: 242px;
    border: 1px solid var(--divider);
    background: var(--header-bg);
  }
  .wall-header {
    position: absolute; left: 0; top: 0;
    width: 100%; height: 52px;
    display: grid;
    grid-template-columns: repeat(12, 1fr);
  }
  .panel-label {
    border-right: 1px solid #edf0f3;
    color: var(--navy);
    font-weight: 700;
    font-size: 11px;
    line-height: 15px;
    letter-spacing: 0.2px;
    text-align: center;
    padding-top: 8px;
  }
  .panel-label:last-child { border-right: none; }
  .panel-label.brand {
    display: flex; flex-direction: column; align-items: center;
    gap: 4px; padding-top: 8px;
    color: var(--brand-cyan);
    font-weight: 400; font-size: 11px;
  }
  .brand-dot {
    width: 16px; height: 16px; border-radius: 50%;
    background: var(--brand-cyan);
  }
  .wall-scene {
    position: absolute; left: 0; top: 52px;
    width: 100%; height: 190px;
    background: linear-gradient(to bottom,
      var(--sky-top) 0%, var(--sky-mid) 28%, var(--horizon) 37%,
      var(--sea-top) 38.5%, var(--sea-mid) 55%, var(--sea-deep) 78%, var(--sea-floor) 100%);
  }
  .panel-dividers {
    position: absolute; inset: 0;
    display: grid; grid-template-columns: repeat(12, 1fr);
  }
  .panel-dividers span { border-right: 1px solid rgba(255,255,255,0.35); }
  .panel-dividers span:last-child { border-right: none; }
  .target {
    position: absolute;
    width: 28px; height: 28px;
    margin: -14px 0 0 -14px;
  }
</style>
</head>
<body>
  <section class="wall" aria-label="Booth wall artwork">
    <header class="wall-header">
      <div class="panel-label brand"><span class="brand-dot"></span>Coral Meridian</div>
      <div class="panel-label">SOVEREIGN<br>SOLUTIONS</div>
      <div class="panel-label">DEPLOYABLE</div>
      <div class="panel-label">UNDERWATER</div>
      <div class="panel-label">ON WATER</div>
      <div class="panel-label">ABOVE WATER</div>
      <div class="panel-label brand"><span class="brand-dot"></span>Coral Meridian</div>
      <div class="panel-label">SOVEREIGN<br>SOLUTIONS</div>
      <div class="panel-label">DEPLOYABLE</div>
      <div class="panel-label">UNDERWATER</div>
      <div class="panel-label">ON WATER</div>
      <div class="panel-label">ABOVE WATER</div>
    </header>

    <div class="wall-scene" role="img" aria-label="Panoramic photo of blue sky with clouds over the ocean horizon, fading into an underwater view with bubbles">
      <div class="panel-dividers">
        <span></span><span></span><span></span><span></span><span></span><span></span>
        <span></span><span></span><span></span><span></span><span></span><span></span>
      </div>

      <svg width="0" height="0" style="position:absolute">
        <symbol id="crosshair" viewBox="0 0 28 28">
          <g fill="none" stroke="var(--target-red)" stroke-width="2">
            <circle cx="14" cy="14" r="6"/>
            <line x1="14" y1="0" x2="14" y2="28"/>
            <line x1="0" y1="14" x2="28" y2="14"/>
          </g>
        </symbol>
      </svg>

      <svg class="target" style="left:4.4%;top:26%"><use href="#crosshair"/></svg>
      <svg class="target" style="left:20.5%;top:37%"><use href="#crosshair"/></svg>
      <svg class="target" style="left:29.5%;top:11%"><use href="#crosshair"/></svg>
      <svg class="target" style="left:40.3%;top:76%"><use href="#crosshair"/></svg>
      <svg class="target" style="left:53.4%;top:26%"><use href="#crosshair"/></svg>
      <svg class="target" style="left:69.4%;top:37%"><use href="#crosshair"/></svg>
      <svg class="target" style="left:78.6%;top:11%"><use href="#crosshair"/></svg>
      <svg class="target" style="left:89.2%;top:76%"><use href="#crosshair"/></svg>
    </div>
  </section>
</body>
</html>
```